Book cover for "Skinward Turning"

Hi, we need a book cover for "Skinward Turning" book.
It's a book about how to cure psoriasis symptoms which appeared to be results of stress.
The main theme in this book is that all symptoms are psychosomatic and can be cut short by reducing the level of stress.
Cover has to be bold and speaking. It has to show the results,
PLEASE consider using photos or illustrations "before" and "after".
Or maybe you can propose your vision.

3D image and 2D image.
Please see the links, it will be helpful for you to create image form.
http://kw7rnpfa.lintrova.com/?skip-tracking=true
http://zt3mxbvc.lintrova.com/?skip-tracking=true

Target Market(s)

TA is very wide, it's all people who experienced decease demonstration. Usually these people very embarrassed of their illness, they are under high level of stress and what they need it's hope and believe that they can relief their condition.

Requirements
Must have
• Author name:
Oleg Varnik
Titlle :
Skinward Turning
Subtitle:
SKINWARD TURNING:
REDUCE THE RASH AND ITCHING 73% WITH THIS SIMPLE TECHNIQUE

```html
<!DOCTYPE html>
<html lang="en">
<head>
<meta charset="utf-8">
<title>Skinward Turning — Book Cover</title>
<link href="https://fonts.googleapis.com/css2?family=Barlow:wght@400;600&family=Libre+Baskerville:wght@700&display=swap" rel="stylesheet">
<style>
  :root {
    --stage: #a9bcd8;
    --paper: #ffffff;
    --subtitle-blue: #1b8ec2;
    --title-blue: #1a7fb8;
    --author-maroon: #8c3b4c;
    --splash-pink: #ec5f9c;
    --splash-rose: #f6b9d2;
    --splash-blue: #2f9fda;
    --ring: #d9dbe8;
  }
  * { margin: 0; padding: 0; box-sizing: border-box; }
  html, body {
    width: 1100px;
    height: 1200px;
    overflow: hidden;
    background: var(--stage);
  }
  .cover {
    position: absolute;
    left: 200px;
    top: 150px;
    width: 700px;
    height: 900px;
    background: var(--paper);
  }
  .cover__subtitle {
    position: absolute;
    top: 52px;
    left: 0;
    width: 100%;
    text-align: center;
    font-family: "Barlow", Arial, sans-serif;
    font-weight: 400;
    font-size: 28px;
    line-height: 38px;
    letter-spacing: 0.5px;
    color: var(--subtitle-blue);
    text-transform: uppercase;
  }
  .cover__subtitle strong { font-weight: 600; }
  .cover__splash {
    position: absolute;
    left: 55px;
    top: 165px;
    width: 590px;
    height: 590px;
  }
  .cover__emblem {
    position: absolute;
    left: 350px;
    top: 460px;
    width: 0;
    height: 0;
  }
  .cover__ring {
    position: absolute;
    left: -132px;
    top: -132px;
    width: 264px;
    height: 264px;
    border-radius: 50%;
    border: 10px solid var(--ring);
    opacity: 0.75;
  }
  .cover__disc {
    position: absolute;
    left: -110px;
    top: -110px;
    width: 220px;
    height: 220px;
    border-radius: 50%;
    background: var(--paper);
    box-shadow: 0 4px 14px rgba(60, 60, 90, 0.18);
    display: flex;
    flex-direction: column;
    align-items: center;
    justify-content: center;
  }
  .cover__title {
    font-family: "Libre Baskerville", Georgia, serif;
    font-weight: 700;
    color: var(--title-blue);
    text-align: center;
    line-height: 1;
  }
  .cover__title-main { display: block; font-size: 31px; letter-spacing: -0.5px; }
  .cover__title-sub { display: block; font-size: 15px; letter-spacing: 1.5px; margin-top: 4px; }
  .cover__author {
    position: absolute;
    bottom: 40px;
    left: 0;
    width: 100%;
    text-align: center;
    font-family: "Barlow", Arial, sans-serif;
    font-weight: 600;
    font-size: 26px;
    letter-spacing: 4px;
    color: var(--author-maroon);
    text-transform: uppercase;
  }
</style>
</head>
<body>
  <main class="cover">
    <p class="cover__subtitle">Reduce the rash and itching<br><strong>73%</strong> with this simple technique</p>

    <svg class="cover__splash" viewBox="0 0 590 590" role="img" aria-label="Watercolour ink splashes in pink and blue surrounding the title circle">
      <defs>
        <radialGradient id="splashWash" cx="50%" cy="50%" r="50%">
          <stop offset="0%" stop-color="#f7c6dc" stop-opacity="0.9"/>
          <stop offset="45%" stop-color="#ec6fa6" stop-opacity="0.75"/>
          <stop offset="70%" stop-color="#7fb8e6" stop-opacity="0.55"/>
          <stop offset="100%" stop-color="#f6b9d2" stop-opacity="0"/>
        </radialGradient>
      </defs>
      <circle cx="295" cy="295" r="295" fill="url(#splashWash)"/>
    </svg>

    <div class="cover__emblem">
      <div class="cover__ring"></div>
      <div class="cover__disc">
        <h1 class="cover__title">
          <span class="cover__title-main">SKINWARD</span>
          <span class="cover__title-sub">TURNING</span>
        </h1>
      </div>
    </div>

    <p class="cover__author">Oleg Varnik</p>
  </main>
</body>
</html>
```